I need a colour and mono poster design promoting our inaugural concert on December 14th 2013. Venue : The Harwell Chapel. at 6pm. Admission is FREE

The programme we will sing is the 'Garland of Hymns' by Gregory Tamsworth
Accompanied by Marisol Petrak on Concert Harp

I would like the main graphic ie Velmora Children's Choir to look more child-friendly, and imagery childlike drawings. Not babyish but not serious either.

Additional visual information for you : the 26 choristers aged 7-14 years, mixed boys and girls and mixed nationalities wear red robes and are accompanied by a concert harpist.

The final design should attract families and children to attend.

Target Market(s)

Families and Press

Requirements
Must have
• A design that works in reduced format for posting on QZ and other social media

```html
<!DOCTYPE html>
<html lang="en">
<head>
<meta charset="utf-8">
<title>Velmora Children's Choir — Inaugural Concert</title>
<link rel="stylesheet" href="https://fonts.googleapis.com/css2?family=Fredoka:wght@600&family=Josefin+Sans:wght@400;600;700&family=Open+Sans:wght@400;700&display=swap">
<style>
  :root {
    --ink: #111111;
    --paper: #ffffff;
    --mist-light: #fbfbfb;
    --mist-dark: #c9c9c9;
    --art-light: #f1f1f1;
    --art-dark: #d6d6d6;
    --muted: #d8d8d8;
  }
  * { margin: 0; padding: 0; box-sizing: border-box; }
  html, body { width: 889px; height: 1200px; overflow: hidden; }
  body { background: var(--paper); }
  .poster {
    position: relative;
    width: 889px;
    height: 1200px;
    overflow: hidden;
    background: radial-gradient(ellipse at 50% 45%, var(--mist-light) 0%, var(--mist-light) 35%, var(--mist-dark) 100%);
  }
  .bands { position: absolute; inset: 0; }
  .choir-name {
    position: absolute;
    top: 40px; left: 0; width: 100%;
    text-align: center;
    font-family: "Fredoka", sans-serif;
    font-weight: 600;
    font-size: 56px;
    color: var(--paper);
    letter-spacing: 0.5px;
  }
  .choir-art {
    position: absolute;
    left: 260px; top: 170px;
    width: 470px; height: 430px;
    border-radius: 40% 40% 30% 30%;
    background: radial-gradient(ellipse at 50% 45%, var(--art-light), var(--art-dark));
  }
  .event {
    position: absolute;
    left: 190px; top: 612px;
    width: 530px;
    font-family: "Josefin Sans", sans-serif;
    color: var(--ink);
  }
  .rule { height: 3px; background: var(--ink); }
  .when { display: flex; align-items: center; justify-content: space-between; padding: 14px 0 4px; }
  .date { font-weight: 700; font-size: 50px; line-height: 50px; }
  .date .day { font-weight: 400; }
  .time { font-weight: 400; font-size: 128px; line-height: 100px; padding-top: 16px; }
  .venue { font-weight: 600; font-size: 42px; letter-spacing: 1px; text-align: center; padding: 12px 0 0; }
  .admission {
    position: absolute;
    left: 560px; top: 820px;
    width: 84px; height: 84px;
    border-radius: 50%;
    background: var(--ink);
    color: var(--paper);
    display: flex; flex-direction: column; align-items: center; justify-content: center;
    font-family: "Fredoka", sans-serif;
    font-weight: 600;
    font-size: 13px; line-height: 17px;
    letter-spacing: 0.3px;
    transform: rotate(-22deg);
  }
  .programme {
    position: absolute;
    left: 0; top: 948px; width: 100%;
    text-align: center;
    color: var(--paper);
    font-family: "Open Sans", sans-serif;
  }
  .programme h2 { font-weight: 700; font-size: 30px; margin-bottom: 8px; }
  .programme p { font-size: 19px; line-height: 25px; color: var(--muted); }
  .programme .choristers {
    margin: 24px auto 0;
    width: 800px;
    font-size: 15px; line-height: 22px;
    color: var(--paper);
    text-transform: uppercase;
  }
</style>
</head>
<body>
<main class="poster">
  <svg class="bands" width="889" height="1200" viewBox="0 0 889 1200" aria-hidden="true">
    <path fill="var(--ink)" d="M0 0 H889 V150 C720 185 600 120 440 150 C280 180 140 130 0 165 Z"/>
    <path fill="var(--ink)" d="M0 930 C160 890 300 935 450 912 C610 885 740 905 889 885 V1200 H0 Z"/>
  </svg>

  <h1 class="choir-name">Velmora Children's Choir</h1>

  <div class="choir-art" role="img" aria-label="Cartoon drawing of children singing in a choir, holding song books"></div>

  <section class="event">
    <div class="rule"></div>
    <div class="when">
      <div class="date">DECEMBER<br><span class="day">14TH 2013</span></div>
      <div class="time">6PM</div>
    </div>
    <div class="rule"></div>
    <div class="venue">THE HARWELL CHAPEL</div>
  </section>

  <div class="admission"><span>ADMISSION</span><span>FREE</span></div>

  <section class="programme">
    <h2>PRESENTING:</h2>
    <p>The Garland of Hymns by Gregory Tamsworth</p>
    <p>Conducted by Irena Voss</p>
    <p>Accompanied by Marisol Petrak on concert harp</p>
    <p class="choristers">The 26 choristers aged 7-14 years, mixed boys and girls and mixed nationalities wear red robes and are accompanied by a concert harpist.</p>
  </section>
</main>
</body>
</html>
```